Corvane Holdings , new business card design

investment firm with corporate clients . need double sided business card , vertical and horizontal options ,logo must be clear. prefer pantone colors only and sharp design. website also www.corvane-example.ae

Khalid Bin Rashed
Managing Director
Tel. +971 4 000 3829
Mobile +971 50 000 4172
khalid@corvane-example.ae
Palm Crest Tower, officw 18-B07, Qasr Gardens, Dubai

Contact Information for Business Card

Khalid Bin Rashed
Managing Director

Font styles to use
Serif

Colors

Designer to choose colors to be used in the design.

```html
<!DOCTYPE html>
<html lang="en">
<head>
<meta charset="utf-8">
<title>Corvane Holdings – Business Card</title>
<link rel="stylesheet" href="https://fonts.googleapis.com/css2?family=Alegreya:wght@400;500&display=swap">
<style>
  :root {
    --page: #ffffff;
    --card-light: #e1e1e1;
    --slate: #64717e;
    --ink-strong: #6a7380;
    --ink-soft: #8d939b;
  }
  html, body {
    margin: 0;
    padding: 0;
    width: 1200px;
    height: 391px;
    overflow: hidden;
    background: var(--page);
  }
  .canvas {
    position: relative;
    width: 1200px;
    height: 391px;
    font-family: "Alegreya", Georgia, serif;
  }
  .card {
    position: absolute;
    top: 22px;
    width: 535px;
    height: 346px;
    background: var(--card-light);
    overflow: hidden;
  }
  .card--front { left: 19px; }
  .card--back { left: 646px; }

  .front-band {
    position: absolute;
    left: 0;
    right: 0;
    top: 186px;
    bottom: 0;
    background: var(--slate);
  }
  .brand-name {
    position: absolute;
    left: 0;
    right: 0;
    top: 142px;
    margin: 0;
    text-align: center;
    font-size: 27px;
    font-weight: 400;
    letter-spacing: 0.3em;
    padding-left: 0.3em;
    color: var(--slate);
    line-height: 1;
    white-space: nowrap;
  }

  .back-block {
    position: absolute;
    left: 72px;
    margin: 0;
    letter-spacing: 0.14em;
    white-space: nowrap;
  }
  .holder { top: 76px; }
  .holder-name {
    display: block;
    font-size: 17px;
    font-weight: 500;
    color: var(--ink-strong);
    line-height: 22px;
  }
  .holder-role {
    display: block;
    font-size: 17px;
    font-weight: 400;
    color: var(--ink-soft);
    line-height: 22px;
  }
  .contact, .office {
    font-size: 14px;
    line-height: 22.5px;
    color: var(--ink-soft);
    font-style: normal;
  }
  .contact { top: 139px; }
  .office { top: 229px; }
  .contact .label {
    color: var(--ink-strong);
    font-weight: 500;
    margin-right: 2px;
  }
  .office .company { color: var(--ink-soft); }
  .sep {
    display: inline-block;
    width: 4px;
    height: 4px;
    border: 1px solid var(--ink-soft);
    border-radius: 50%;
    vertical-align: middle;
    margin: 0 4px 2px;
  }
  .website {
    position: absolute;
    left: 508px;
    top: 173px;
    transform: translate(-50%, -50%) rotate(-90deg);
    font-size: 15px;
    letter-spacing: 0.2em;
    color: var(--ink-strong);
    white-space: nowrap;
    margin: 0;
  }
</style>
</head>
<body>
<main class="canvas">
  <section class="card card--front" aria-label="Card front">
    <div class="front-band"></div>
    <h1 class="brand-name">CORVANE HOLDINGS</h1>
  </section>

  <section class="card card--back" aria-label="Card back">
    <p class="back-block holder">
      <span class="holder-name">Khalid Bin Rashed</span>
      <span class="holder-role">Managing Director</span>
    </p>
    <address class="back-block contact">
      khalid@corvane-example.ae<br>
      <span class="label">T</span> +971 4 000 3829<br>
      <span class="label">M</span> +971 50 000 4172
    </address>
    <address class="back-block office">
      <span class="company">CORVANE HOLDINGS</span><br>
      Palm Crest Tower<span class="sep"></span>officw 18-B07<br>
      Qasr Gardens<span class="sep"></span>Dubai
    </address>
    <p class="website">www.corvane-example.ae</p>
  </section>
</main>
</body>
</html>
```